Creative 1 page website design with html coding needed to go with Game Pre-Registration App

Velvet Arcade Club
~Discover games before release~

Website keywords: Simple, slick, stylish
Colors: Black, white, pink (like our logo)

***draft can be created in PSD or HTML***

We have a brand new service called Velvet Arcade Club which will be a game app pre-registration service. We already have the icon & UI for the app and we are looking for a slick & stylish corporate website to go with the service.

This will be a corporate website aim for businesses to contact us. Consumers will not be able to pre-register for games here. We do however want consumers to download our app from Zorvik Shelf after landing here.

Some framework we have in mind for 1 page website:
Home - default page showing the UI of the app and Zorvik Shelf icon with store link.
Our Service - quick explanation about our service & it's strength
Clients - logos of our clients
Press-
Pricing - basic usage is free. There will be premium services customers can use on a performance basis (CPA).
Contact Us

Call to action will be 1. Download the app 2. Contact us

We would like to be able to edit the press and clients section with web developer's support.

website in image:
https://www.marlowbyte.com/

Target Market(s)

Marketing managers of game developer. We want game developers to find out about our service and get in touch with us. The service will only be available in USA.

Midcore gamers in USA: Our end users will be game enthusiasts from US. Male aged 15-35.

Industry/Entity Type

Games

Font styles to use
Sans Serif

Colors
000000
ffffff
e567a6
e34097

Requirements
Must have
• - Only use our colors from the logo attached.
- UI of our app with an Quilbo phone
- Link to Zorvik Shelf Store
- slick & modern design
- Font used: Century Gothic

```html
<!DOCTYPE html>
<html lang="en">
<head>
<meta charset="utf-8">
<title>Velvet Arcade Club</title>
<link rel="stylesheet" href="https://fonts.googleapis.com/css2?family=Lobster&family=Roboto:wght@400;500;700&family=Questrial&display=swap">
<style>
:root{
  --pink:#e34097;
  --pink-light:#e567a6;
  --pink-deep:#a3135f;
  --black:#000;
  --white:#fff;
  --screen:#2b2b2d;
}
*{margin:0;padding:0;box-sizing:border-box}
html,body{width:1200px;height:821px;overflow:hidden;background:var(--black)}
body{position:relative;font-family:"Roboto",sans-serif;color:var(--white)}
a{color:inherit;text-decoration:none}
.abs{position:absolute}
.top-line{left:0;top:0;width:1200px;height:3px;background:var(--pink)}
.hero-scene{left:0;top:3px;width:1200px;height:615px;
  background:linear-gradient(180deg,#3a3640 0%,#4c3a4a 20%,#5a4356 28%,#2d2b33 45%,#1d1c22 75%,#15141a 100%)}
.header{left:0;top:3px;width:1200px;height:105px;background:rgba(60,55,60,.45)}
.brand{left:172px;top:19px;display:flex;align-items:center;gap:10px}
.brand-mark{width:50px;height:50px;border-radius:8px;background:linear-gradient(180deg,var(--pink-light),var(--pink))}
.brand-name{font-family:"Questrial",sans-serif;font-size:25px;color:var(--white)}
.nav a{position:absolute;top:39px;font-size:13.5px;line-height:25px;white-space:nowrap}
.nav a.active{border:1px solid var(--pink);border-radius:3px;color:var(--pink-light);padding:0 11px;line-height:23px;height:25px}
.ring{border:1px solid rgba(255,255,255,.45);border-radius:50%}
.hero-title{left:172px;top:190px;font-family:"Lobster",sans-serif;font-weight:400;font-size:38px;white-space:nowrap;text-shadow:2px 2px 3px rgba(0,0,0,.6)}
.hero-copy{left:176px;top:259px;width:514px;font-size:18px;line-height:35px;text-align:justify}
.btn{height:55px;border-radius:8px;font-size:19px;display:flex;align-items:center;justify-content:center;color:var(--white)}
.btn-download{left:176px;top:439px;width:248px;background:linear-gradient(180deg,var(--pink-light),#c0237a);box-shadow:0 3px 6px rgba(0,0,0,.5)}
.btn-contact{left:438px;top:440px;width:184px;background:linear-gradient(180deg,#4a8fc0,#2d6a96);box-shadow:0 3px 6px rgba(0,0,0,.5)}
.arrow-ring{width:40px;height:40px;border:3px solid rgba(255,255,255,.75);border-radius:50%;display:flex;align-items:center;justify-content:center}
.band{left:0;top:618px;width:1200px;height:63px;background:var(--pink)}
.band-deep{left:0;top:681px;width:1200px;height:14px;background:var(--pink-deep)}
.store{top:586px;height:66px;background:var(--black);border:1px solid #888;border-radius:6px;box-shadow:0 8px 10px rgba(0,0,0,.35);display:flex;align-items:center;padding-left:14px;gap:12px;color:var(--white)}
.store-mark{width:32px;height:32px;border-radius:50%;background:#555;flex:none}
.store-text{display:flex;flex-direction:column;white-space:nowrap}
.store-small{font-size:8px;letter-spacing:.5px;line-height:10px}
.store-big{font-size:25px;line-height:28px}
.phone{left:748px;top:130px;width:260px;height:525px;border-radius:46px;background:linear-gradient(90deg,#222,#111 40%,#1c1c1c);border:3px solid #8a8a8a;box-shadow:0 14px 20px rgba(0,0,0,.45)}
.speaker{left:100px;top:22px;width:60px;height:5px;border-radius:3px;background:#444}
.screen{left:16px;top:62px;width:229px;height:402px;background:var(--screen);overflow:hidden;font-family:"Questrial",sans-serif}
.status{left:0;top:0;width:229px;height:18px;background:#111;font-size:10px;text-align:right;padding-right:6px;line-height:18px}
.appbar{left:0;top:18px;width:229px;height:32px;background:#1e1e1e;display:flex;align-items:center;gap:6px;padding-left:16px;font-size:15px}
.appbar .mini{width:18px;height:18px;border-radius:3px;background:var(--pink)}
.tabs{left:0;top:50px;width:229px;height:24px;background:#1e1e1e;font-size:13px;color:#ddd}
.tabs span{position:absolute;top:4px}
.tab-line{left:0;top:71px;width:67px;height:3px;background:var(--pink)}
.row{left:0;width:229px;height:126px;border-bottom:2px solid #555}
.thumb{left:15px;top:14px;width:95px;height:95px;border-radius:8px}
.g-title{left:120px;top:16px;font-size:11px;font-weight:bold;color:var(--white);white-space:nowrap}
.g-meta{left:120px;top:32px;font-size:8px;line-height:10px;color:#ccc;white-space:nowrap}
.rank{left:4px;top:50px;font-size:12px;color:#ccc}
.chip{height:14px;padding:0 4px;font-size:7px;line-height:14px;background:var(--pink);color:var(--white)}
.softkeys{left:0;top:372px;width:229px;height:30px;background:#111}
.footer-brand{left:174px;top:745px;display:flex;align-items:center;gap:8px}
.footer-brand .brand-mark{width:28px;height:28px;border-radius:5px}
.footer-brand .brand-name{font-size:19px}
.copyright{left:797px;top:754px;font-size:13px;color:#ddd}
.bottom-line{left:0;top:817px;width:1200px;height:4px;background:var(--pink)}
</style>
</head>
<body>
<div class="abs top-line"></div>
<div class="abs hero-scene" role="img" aria-label="Night city skyline photograph under a dusky pink sky"></div>

<header class="abs header">
  <div class="abs brand"><span class="brand-mark"></span><span class="brand-name">Velvet Arcade Club</span></div>
  <nav class="nav">
    <a class="active" href="#" style="left:485px">HOME</a>
    <a href="#" style="left:562px">SERVICESS</a>
    <a href="#" style="left:658px">CLIENTS</a>
    <a href="#" style="left:738px">PRESS</a>
    <a href="#" style="left:807px">CONTACT US</a>
  </nav>
  <span class="abs ring" style="left:908px;top:37px;width:30px;height:30px" aria-label="Social link"></span>
  <span class="abs ring" style="left:951px;top:37px;width:30px;height:30px" aria-label="Social link"></span>
  <span class="abs ring" style="left:995px;top:37px;width:30px;height:30px" aria-label="Social link"></span>
</header>

<h1 class="abs hero-title">Welcome to Velvet Arcade Club</h1>
<p class="abs hero-copy">Lorem Ipsum is simply dummy text of the printing and typesetting industry. Lorem Ipsum has been the industry's standard dummy text ever since the 1500s, when an unknown printer took a galley of type and scrambled it to make a type</p>

<a class="abs btn btn-download" href="#">DOWNLOAD THE&nbsp;<b>APP</b></a>
<a class="abs btn btn-contact" href="#">CONTACT US</a>

<div class="abs arrow-ring" style="left:51px;top:340px"><svg width="14" height="14" viewBox="0 0 14 14"><path d="M9 2 L4 7 L9 12" fill="none" stroke="#fff" stroke-width="2.5"/></svg></div>
<div class="abs arrow-ring" style="left:1114px;top:349px"><svg width="14" height="14" viewBox="0 0 14 14"><path d="M5 2 L10 7 L5 12" fill="none" stroke="#fff" stroke-width="2.5"/></svg></div>

<div class="abs band"></div>
<div class="abs band-deep"></div>

<a class="abs store" style="left:178px;width:203px" href="#">
  <span class="store-mark"></span>
  <span class="store-text"><span class="store-small">QUILBO APP ON</span><span class="store-big">Zorvik Shelf</span></span>
</a>
<a class="abs store" style="left:417px;width:196px" href="#">
  <svg width="24" height="42" viewBox="0 0 26 44" style="flex:none"><rect x="2" y="2" width="22" height="40" rx="4" fill="none" stroke="#fff" stroke-width="3"/><rect x="6" y="8" width="14" height="26" fill="#fff"/></svg>
  <span class="store-text"><span style="font-size:15px;line-height:18px">Available on the</span><span class="store-big" style="font-size:21px">Orchard Depot</span></span>
</a>

<div class="abs phone">
  <div class="abs speaker"></div>
  <div class="abs screen">
    <div class="abs status">1:54 PM</div>
    <div class="abs appbar"><span class="mini"></span><span>Velvet Arcade</span></div>
    <div class="abs tabs"><span style="left:10px">Overall</span><span style="left:85px">Buzz</span><span style="left:152px">New</span></div>
    <div class="abs tab-line"></div>

    <div class="abs row" style="top:76px">
      <span class="abs rank">1</span>
      <div class="abs thumb" role="img" aria-label="Game artwork: fiery dragon" style="background:linear-gradient(135deg,#c56a2a,#5a2010)"></div>
      <div class="abs g-title">Ember Wyrm Saga</div>
      <div class="abs g-meta">Kilnforge Inc.<br>October 2014</div>
      <span class="abs chip" style="left:178px;top:92px">8.5K</span>
    </div>
    <div class="abs row" style="top:202px">
      <span class="abs rank">1</span>
      <div class="abs thumb" role="img" aria-label="Game artwork: island adventure" style="background:linear-gradient(135deg,#3aa0d8,#7a5a3a)"></div>
      <div class="abs g-title">Tidebreak Isle</div>
      <div class="abs g-meta">Northvane<br>Fall 2014</div>
      <span class="abs chip" style="left:178px;top:92px">986</span>
    </div>
    <div class="abs row" style="top:328px;border:none">
      <div class="abs thumb" role="img" aria-label="Game artwork: race car" style="background:linear-gradient(135deg,#eee,#c22)"></div>
      <div class="abs g-title">Vireo Racing</div>
      <div class="abs g-meta">Quickgrain Motion<br>Spring 2015</div>
    </div>
    <div class="abs softkeys"></div>
  </div>
</div>

<footer>
  <div class="abs footer-brand"><span class="brand-mark"></span><span class="brand-name">Velvet Arcade Club</span></div>
  <span class="abs ring" style="left:512px;top:738px;width:44px;height:44px;border-color:#999" aria-label="Social link"></span>
  <span class="abs ring" style="left:578px;top:738px;width:44px;height:44px;border-color:#999" aria-label="Social link"></span>
  <span class="abs ring" style="left:644px;top:738px;width:44px;height:44px;border-color:#999" aria-label="Social link"></span>
  <p class="abs copyright">Copyright © 2014&nbsp; All Rights Reserved</p>
  <div class="abs bottom-line"></div>
</footer>
</body>
</html>
```